Word document template for sales proposals

I am after a template that is simple but impactful. Use of colour to be limited but some for impact would be good. The proposals are for use in the professional technical field.

```html
<!DOCTYPE html>
<html lang="en">
<head>
<meta charset="utf-8">
<title>Proposal Letterhead</title>
<link rel="stylesheet" href="https://fonts.googleapis.com/css2?family=Montserrat:wght@300;400;600&family=Open+Sans:wght@400&display=swap">
<style>
  :root {
    --sun: #F9C933;
    --amber: #FA9A14;
    --band: #E4E5E7;
    --ink: #231F20;
    --slate: #6D6E70;
    --muted: #8A8A8C;
    --brand: #E0922F;
    --paper: #FFFFFF;
  }
  * { margin: 0; padding: 0; box-sizing: border-box; }
  html, body { width: 825px; height: 1200px; overflow: hidden; background: var(--paper); }
  .page { position: relative; width: 825px; height: 1200px; overflow: hidden; background: var(--paper); font-family: "Montserrat", sans-serif; }

  .header-band { position: absolute; left: 0; top: 146px; width: 825px; height: 45px; background: var(--band); }
  .header-tab { position: absolute; left: 0; top: 0; }

  .brand { position: absolute; left: 73px; top: 86px; width: 234px; height: 113px; display: flex; align-items: center; justify-content: center; gap: 8px; }
  .brand-dot { width: 14px; height: 14px; border-radius: 50%; background: var(--brand); }
  .brand-name { font-family: "Montserrat", sans-serif; font-weight: 600; font-size: 21px; letter-spacing: 1px; color: var(--brand); }

  .date { position: absolute; right: 98px; top: 254px; font-weight: 600; font-size: 17px; color: var(--slate); }
  .salutation { position: absolute; left: 98px; top: 322px; font-weight: 600; font-size: 23px; color: var(--ink); }

  .body-copy { position: absolute; left: 101px; top: 383px; width: 626px; }
  .body-copy p { font-weight: 300; font-size: 15.4px; line-height: 26.6px; color: var(--muted); text-align: justify; margin-bottom: 36px; }

  .signature { position: absolute; left: 99px; top: 840px; font-family: "Open Sans", sans-serif; font-size: 68px; line-height: 86px; color: var(--ink); }
  .signer-name { position: absolute; left: 101px; top: 923px; font-weight: 600; font-size: 25.5px; color: var(--ink); }
  .signer-role { position: absolute; left: 101px; top: 960px; font-weight: 400; font-size: 19px; color: var(--slate); }

  .contact-list { position: absolute; right: 96px; top: 986px; list-style: none; }
  .contact-item { display: flex; align-items: center; justify-content: flex-end; gap: 15px; height: 29px; font-family: "Open Sans", sans-serif; font-size: 10.5px; color: var(--slate); }
  .contact-icon { width: 20px; height: 20px; border-radius: 50%; background: var(--amber); display: flex; align-items: center; justify-content: center; }
  .contact-icon svg { width: 12px; height: 12px; fill: none; stroke: var(--paper); stroke-width: 1.4; stroke-linecap: round; stroke-linejoin: round; }

  .footer-band { position: absolute; left: 0; top: 1160px; width: 420px; height: 40px; background: var(--band); }
  .footer-panel { position: absolute; left: 407px; top: 1142px; width: 344px; height: 58px; background: var(--sun); border-top-left-radius: 31px; }
  .footer-accent { position: absolute; left: 751px; top: 1142px; width: 74px; height: 58px; background: var(--amber); }
</style>
</head>
<body>
<div class="page">
  <div class="header-band"></div>
  <svg class="header-tab" width="400" height="210" viewBox="0 0 400 210" aria-hidden="true">
    <path d="M73 86 H361 L333 146 Q305 199 268 199 H73 Z" fill="var(--sun)"/>
    <rect x="58" y="86" width="15" height="113" fill="var(--amber)"/>
    <path d="M361 86 L371 146 H333 Z" fill="var(--amber)"/>
  </svg>

  <div class="brand">
    <span class="brand-dot"></span>
    <span class="brand-name">BRIGHTWELL</span>
  </div>

  <div class="date">Date August 28, 2022</div>
  <div class="salutation">Dear Thomas Avery</div>

  <div class="body-copy">
    <p>Lorem ipsum dolor sit amet, consectetuer adipiscing elit, sed diam nonummy nibh euismod tincidunt ut laoreet dolore magna aliquam erat volutpat. Ut wisi enim ad minim veniam, quis nostrud exerci tation ullamcorper suscipit lobortis nisl ut aliquip ex ea commodo consequat.</p>
    <p>Duis autem vel eum iriure dolor in hendrerit in vulputate velit esse molestie consequat, vel illum dolore eu feugiat nulla facilisis at vero eros et accumsan et iusto odio dignissim qui blandit praesent luptatum zzril delenit augue duis dolore te feugait nulla facilisi.</p>
    <p>Lorem ipsum dolor sit amet, consectetuer adipiscing elit, sed diam nonummy nibh euismod tincidunt ut laoreet dolore magna aliquam erat volutpat. Ut wisi enim ad minim veniam, quis nostrud exerci tation ullamcorper suscipit lobortis nisl ut aliquip ex ea commodo consequat.</p>
  </div>

  <div class="signature">Martin</div>
  <div class="signer-name">Martin Hale</div>
  <div class="signer-role">Manager</div>

  <ul class="contact-list">
    <li class="contact-item">YOUR ADRESS GOES HERE
      <span class="contact-icon"><svg viewBox="0 0 12 12"><path d="M1.5 6 L6 2 L10.5 6 M2.8 5 V10 H9.2 V5 M5 10 V7.5 H7 V10"/></svg></span></li>
    <li class="contact-item">YOURWEB@EMAIL.COM
      <span class="contact-icon"><svg viewBox="0 0 12 12"><rect x="1.5" y="3" width="9" height="6.5" rx="0.8"/><path d="M1.8 3.4 L6 6.6 L10.2 3.4"/></svg></span></li>
    <li class="contact-item">+123 456789
      <span class="contact-icon"><svg viewBox="0 0 12 12"><path d="M3 1.8 L4.6 3.6 L3.8 4.8 Q5 7 7.2 8.2 L8.4 7.4 L10.2 9 L9.2 10.2 Q5.5 10 2.8 6.8 Q1.6 4.8 1.9 2.8 Z"/></svg></span></li>
    <li class="contact-item">YOURWEBSITE.COM
      <span class="contact-icon"><svg viewBox="0 0 12 12"><circle cx="6" cy="6" r="4.5"/><ellipse cx="6" cy="6" rx="2" ry="4.5"/><path d="M1.5 6 H10.5 M2.2 3.8 H9.8 M2.2 8.2 H9.8"/></svg></span></li>
  </ul>

  <div class="footer-band"></div>
  <div class="footer-panel"></div>
  <div class="footer-accent"></div>
</div>
</body>
</html>
```